BrimKeel Limited needs a business card design

We need a business card design that reflects both professionalism and innovation and captures our brand identity. We provide online enterprise solutions to HR and executive management. We would like to use the colors in our logo (Blue and Orange). See attached file.

We would like a more creative design than the existing attached business card but maintain the same information on it.

To see our products site, please visit www.brimkeel.example which reflects more our identity
Updates

Please see our site: www.brimkeel.example, not www.brimkeel.example.co.uk for our colors and look and feel

Target Market(s)

Senior Executives

Industry/Entity Type

Business

Requirements
Must have
• Logo and use of logo colors
Nice to have
• Icons
Should not have
• Images

```html
<!DOCTYPE html>
<html lang="en">
<head>
<meta charset="utf-8">
<title>BrimKeel Limited – Business Card</title>
<link rel="stylesheet" href="https://fonts.googleapis.com/css2?family=Questrial&display=swap">
<style>
  :root {
    --bg: #e8e6e2;
    --card: #ffffff;
    --blue: #1f6fb7;
    --orange: #f0883a;
    --ink: #4a4a4a;
    --grey: #6d6d6d;
    --grey-light: #8a8a8a;
    --shadow: rgba(0, 0, 0, 0.14);
  }
  * { margin: 0; padding: 0; box-sizing: border-box; }
  html, body {
    width: 1200px; height: 1184px; overflow: hidden;
    background: var(--bg);
    font-family: "Questrial", "Century Gothic", sans-serif;
    color: var(--grey);
  }
  .card {
    position: absolute; left: 160px;
    width: 880px; height: 503px;
    background: var(--card);
    box-shadow: 0 10px 30px var(--shadow);
  }
  .card--front { top: 60px; text-align: center; }
  .card--back { top: 621px; }

  /* Brand name: one colour, one weight, no accent */
  .brand {
    font-weight: 400;
    color: var(--ink);
    line-height: 1;
    white-space: nowrap;
  }

  /* Front */
  .company-name {
    margin-top: 52px;
    font-size: 34px; font-weight: 400; color: var(--orange);
  }
  .tagline {
    margin-top: 12px;
    font-size: 15px; letter-spacing: 2.5px; color: var(--grey);
  }
  .card--front .brand { margin-top: 40px; font-size: 130px; }
  .registration {
    margin-top: 36px;
    font-size: 15px; line-height: 1.7; color: var(--grey-light); letter-spacing: 0.5px;
  }

  /* Back */
  .card--back .brand {
    position: absolute; left: 56px; top: 52px;
    font-size: 80px;
  }
  .person { position: absolute; left: 60px; top: 200px; }
  .person__name { font-size: 30px; font-weight: 400; letter-spacing: 1px; }
  .person__first { color: var(--blue); }
  .person__last { color: var(--orange); }
  .person__role {
    font-size: 16px; letter-spacing: 3px; color: var(--grey); margin-top: 2px;
  }
  .contacts {
    position: absolute; left: 110px; top: 300px;
    display: grid; grid-template-columns: 42px auto; row-gap: 6px;
    font-size: 19px; letter-spacing: 1px;
  }
  .contacts dt { color: var(--blue); }
  .contacts dd { color: var(--grey); }
  .contacts .gap { margin-top: 14px; }
  .address {
    position: absolute; left: 520px; top: 200px;
    font-size: 19px; line-height: 1.55; letter-spacing: 0.5px; color: var(--grey);
    font-style: normal;
  }
</style>
</head>
<body>
  <section class="card card--front" aria-label="Business card front">
    <h1 class="company-name">BrimKeel Limited</h1>
    <p class="tagline">DEVELOPING LEADERS AND ORGANISATIONS</p>
    <p class="brand">BrimKeel</p>
    <p class="registration">
      BrimKeel Limited is a company registered in England &amp; Wales<br>
      Registered Office: Harbour House, London
    </p>
  </section>

  <section class="card card--back" aria-label="Business card back">
    <p class="brand">BrimKeel</p>

    <div class="person">
      <h2 class="person__name"><span class="person__first">MARA</span><span class="person__last">VELLIN</span></h2>
      <p class="person__role">MANAGING DIRECTOR</p>
    </div>

    <dl class="contacts">
      <dt>T.</dt><dd>+44 20 0000 1234</dd>
      <dt></dt><dd>+1 555 010 2468</dd>
      <dt></dt><dd>+961 70 000 135</dd>
      <dt class="gap">E.</dt><dd class="gap">mvellin@brimkeel.example.co.uk</dd>
      <dt>W.</dt><dd>www.brimkeel.example.co.uk</dd>
    </dl>

    <address class="address">
      brimkeel limited<br>
      1406 Harrow Court,<br>
      52 Linden St, London, W1X 0AA
    </address>
  </section>
</body>
</html>
```